CV Template

We need a graphic design to our new CV templates for our consultants. We are a small young Danish upcoming IT-business company making software solutions for our customers etc. You can visit our new website here: dev.lunavaerket.com, then you can see our web design, colors etc. I have attached a file for your inspiration :-) In the presentation I would like to have a picture of the employee, some text who descripe the profile/consultant and then I imagine that there is a table where we can write the employee's skills etc.

I would like the design to be "fresh & catchy" :-)

Looking forward to hear from you.

Best regards,
Sanne

```html
<!DOCTYPE html>
<html lang="da">
<head>
<meta charset="utf-8">
<title>CV skabelon – Lunaværket</title>
<link rel="stylesheet" href="https://fonts.googleapis.com/css2?family=Arimo:wght@400;700&family=Open+Sans:wght@400;600&display=swap">
<style>
  :root {
    --navy: #0b2a5c;
    --deep: #1c4f93;
    --mid: #4f86c6;
    --sky: #a9c8ea;
    --mist: #e8f0f9;
    --white: #ffffff;
    --rule: #4aa3df;
    --ink: #111111;
    --grey: #2e2e2e;
  }
  * { box-sizing: border-box; margin: 0; padding: 0; }
  html, body { width: 926px; height: 1200px; overflow: hidden; background: var(--white); }
  .cv-page {
    position: relative;
    width: 926px;
    height: 1200px;
    overflow: hidden;
    font-family: "Open Sans", sans-serif;
    color: var(--ink);
  }
  .backdrop {
    position: absolute; inset: 0;
    background:
      radial-gradient(ellipse 420px 260px at 720px 110px, rgba(255,255,255,.85), rgba(255,255,255,0) 70%),
      radial-gradient(ellipse 520px 420px at 900px 1150px, rgba(255,255,255,.95), rgba(255,255,255,0) 75%),
      linear-gradient(100deg, var(--navy) 0%, var(--deep) 22%, var(--mid) 48%, var(--sky) 75%, var(--mist) 100%);
  }
  .swoosh { position: absolute; inset: 0; }
  .spine {
    position: absolute; left: 108px; top: 0; width: 2px; height: 1200px;
    background: var(--navy); opacity: .8;
  }
  .crossbar {
    position: absolute; left: 108px; top: 220px; width: 818px; height: 1px;
    background: rgba(255,255,255,.7);
  }
  .brand {
    position: absolute; left: 656px; top: 51px; width: 212px; height: 64px;
    background: var(--white);
    display: flex; align-items: center; justify-content: center; gap: 10px;
    font-family: "Arimo", sans-serif; font-size: 24px; font-weight: 400;
    color: var(--navy); letter-spacing: 1px;
  }
  .brand-mark { width: 12px; height: 12px; background: var(--navy); }
  .headline { position: absolute; left: 112px; top: 142px; }
  .portrait {
    position: absolute; left: 56px; top: 334px; width: 177px; height: 127px;
    border: 3px solid var(--white);
    background: radial-gradient(ellipse at 55% 45%, #c9b8a6 0%, #8e8a84 45%, #5f6a76 100%);
    box-shadow: 0 2px 6px rgba(0,0,0,.35);
  }
  .section-label {
    position: absolute; font-size: 19px; font-weight: 400; color: var(--ink);
  }
  .section-label.profile { left: 246px; top: 354px; }
  .section-label.skills { left: 56px; top: 562px; }
  .rule { position: absolute; height: 1px; background: var(--rule); }
  .rule.profile { left: 244px; top: 383px; width: 630px; }
  .rule.skills { left: 49px; top: 591px; width: 825px; }
  .profile-box {
    position: absolute; left: 244px; top: 396px; width: 641px; height: 150px;
    border: 1.5px solid var(--ink);
    padding: 12px 16px;
    font-size: 14px; line-height: 23px; color: var(--ink);
  }
  .skills-table {
    position: absolute; left: 49px; top: 624px; width: 812px; height: 289px;
    border-collapse: collapse; table-layout: fixed;
    font-size: 10.5px; line-height: 15px; color: var(--ink);
  }
  .skills-table td, .skills-table th {
    border: 1px solid var(--ink); height: 17px;
    padding: 0 5px; text-align: left;
    white-space: nowrap; overflow: hidden; text-overflow: ellipsis;
  }
  .skills-table th { font-weight: 600; }
  .quote-box {
    position: absolute; left: 62px; top: 951px; width: 439px; height: 178px;
    border: 1.5px solid var(--ink);
    padding: 8px 34px 8px 10px;
    font-size: 12.5px; line-height: 22px; color: var(--grey);
  }
</style>
</head>
<body>
<div class="cv-page">
  <div class="backdrop" role="img" aria-label="Abstrakt blå baggrund med tastatur og udviklingsværktøjer"></div>
  <svg class="swoosh" width="926" height="1200" viewBox="0 0 926 1200" aria-hidden="true">
    <path d="M110 900 C 300 800, 560 790, 926 860 L 926 1200 L 110 1200 Z" fill="rgba(255,255,255,.18)"/>
    <path d="M110 960 C 340 860, 620 880, 926 980" fill="none" stroke="rgba(255,255,255,.45)" stroke-width="2"/>
  </svg>
  <div class="spine"></div>
  <div class="crossbar"></div>

  <div class="brand"><span class="brand-mark"></span>Lunaværket</div>

  <svg class="headline" width="806" height="48" viewBox="0 0 806 48">
    <text x="4" y="36" textLength="792" lengthAdjust="spacingAndGlyphs"
          font-family="Arimo, sans-serif" font-weight="700" font-size="35"
          fill="#08204a" opacity=".35">Rutineret og erfaren Software udvikler &amp; konsulent</text>
    <text x="2" y="34" textLength="792" lengthAdjust="spacingAndGlyphs"
          font-family="Arimo, sans-serif" font-weight="700" font-size="35"
          fill="#0b2a5c" stroke="#ffffff" stroke-width="1.4" paint-order="stroke">Rutineret og erfaren Software udvikler &amp; konsulent</text>
  </svg>

  <div class="portrait" role="img" aria-label="Portrætfoto af konsulenten"></div>

  <h2 class="section-label profile">Profilbeskrivelse</h2>
  <div class="rule profile"></div>
  <p class="profile-box">Erfaren udvikler med mange års arbejde inden for webudvikling, databaser og integrationer. Leverer stabile løsninger til kunder i både små og store projekter.</p>

  <h2 class="section-label skills">Kompetenceområder</h2>
  <div class="rule skills"></div>
  <table class="skills-table">
    <colgroup>
      <col style="width:60px"><col style="width:140px"><col style="width:163px">
      <col style="width:201px"><col style="width:131px"><col style="width:117px">
    </colgroup>
    <thead>
      <tr><th>Nr</th><th>Område</th><th>Kompetence</th><th>Beskrivelse</th><th>Niveau</th><th>År</th></tr>
    </thead>
    <tbody>
      <tr><td>1</td><td>Udvikling</td><td>Backend</td><td>Webservices og API</td><td>Ekspert</td><td>8</td></tr>
      <tr><td>2</td><td>Udvikling</td><td>Frontend</td><td>Responsive web</td><td>Erfaren</td><td>5</td></tr>
      <tr><td>3</td><td>Data</td><td>Databaser</td><td>Design og drift</td><td>Ekspert</td><td>7</td></tr>
      <tr><td>4</td><td>Rådgivning</td><td>Arkitektur</td><td>Kravspecifikation</td><td>Erfaren</td><td>6</td></tr>
      <tr><td>5</td><td>Ledelse</td><td>Projekter</td><td>Agile forløb</td><td>Øvet</td><td>4</td></tr>
      <tr><td></td><td></td><td></td><td></td><td></td><td></td></tr>
      <tr><td></td><td></td><td></td><td></td><td></td><td></td></tr>
      <tr><td></td><td></td><td></td><td></td><td></td><td></td></tr>
      <tr><td></td><td></td><td></td><td></td><td></td><td></td></tr>
      <tr><td></td><td></td><td></td><td></td><td></td><td></td></tr>
      <tr><td></td><td></td><td></td><td></td><td></td><td></td></tr>
      <tr><td></td><td></td><td></td><td></td><td></td><td></td></tr>
      <tr><td></td><td></td><td></td><td></td><td></td><td></td></tr>
      <tr><td></td><td></td><td></td><td></td><td></td><td></td></tr>
      <tr><td></td><td></td><td></td><td></td><td></td><td></td></tr>
      <tr><td></td><td></td><td></td><td></td><td></td><td></td></tr>
    </tbody>
  </table>

  <p class="quote-box">[Skriv et citat fra dokumentet eller et resumé af et interessant afsnit. Du kan placere tekstfeltet hvor som helst i dokumentet. Brug fanen Tekstfeltværktøjer til at ændre formateringen af citatets tekstfelt.]</p>
</div>
</body>
</html>
```